Fresh Tarrow Work Post - Business Card Required

Dear All,

I own Velmira Limited, which in turn owns the website:
www.harbinworkpost.example

I want all of you wonderful creative people to come up with a slick, and awesome business card design that incorporates the logo on the site, and some colouring and design elements from it.

You have free reign in how you go about doing this, I won't be giving my contact details on this platform, but the winner will be asked to redesign based on my contact details which I will supply at the end.

I need the design to be completed within 5 days. I need the final print copies of the business cards by the 25th November, so unfortunately it's a bit of a rush to get these designs ready.

Any questions, please ask.

Thank you
Updates

Thank you all for your hard work and exceptional designs provided. I do have to pick one, so I have a very clear idea of which one this is, however I will wait one further day until the competition closes to be fair to all those have submitted, or are in the process of submitting. I wish you all the best and thank you again for your dedication.

```html
<!DOCTYPE html>
<html lang="en">
<head>
<meta charset="utf-8">
<title>Fresh Tarrow Work Post – Business Card</title>
<link rel="stylesheet" href="https://fonts.googleapis.com/css2?family=Montserrat:wght@400;500;600&family=Saira+Condensed:wght@600;700&display=swap">
<style>
  :root {
    --backdrop: #5d666c;
    --card: #141414;
    --gold-light: #f3d08a;
    --gold: #c99a4a;
    --gold-deep: #8a5d22;
    --ink: #1a1208;
    --white: #ffffff;
  }
  * { box-sizing: border-box; margin: 0; padding: 0; }
  html, body {
    width: 1200px; height: 843px; overflow: hidden;
    background: var(--backdrop);
  }
  body { display: flex; align-items: center; justify-content: center; }
  .card {
    position: relative;
    width: 1000px; height: 572px;
    background: var(--card);
    overflow: hidden;
    box-shadow: 0 18px 40px rgba(0,0,0,.35);
  }
  .card-trim { position: absolute; inset: 0; width: 100%; height: 100%; }
  .brand {
    position: absolute; left: 60px; top: 238px;
    display: flex; align-items: center; gap: 16px;
  }
  .brand-dot {
    width: 44px; height: 44px; border-radius: 50%;
    background: var(--gold);
  }
  .brand-name {
    font-family: "Montserrat", sans-serif; font-weight: 500;
    font-size: 21px; letter-spacing: 2.5px; text-transform: uppercase;
    color: var(--gold);
  }
  .person { position: absolute; left: 560px; top: 176px; }
  .person-name {
    font-family: "Saira Condensed", sans-serif; font-weight: 700;
    font-size: 60px; line-height: 1; letter-spacing: 3px;
    color: var(--white); text-transform: uppercase;
  }
  .person-role {
    margin-top: 6px;
    font-family: "Montserrat", sans-serif; font-weight: 500;
    font-size: 19px; letter-spacing: 3px; text-transform: uppercase;
    color: var(--white);
  }
  .contacts {
    position: absolute; left: 512px; top: 300px;
    list-style: none; display: flex; flex-direction: column; gap: 12px;
  }
  .contact { display: flex; align-items: center; gap: 14px; }
  .contact-icon {
    width: 32px; height: 32px; border-radius: 50%;
    border: 2px solid var(--gold); display: flex;
    align-items: center; justify-content: center;
  }
  .contact-icon svg { width: 16px; height: 16px; fill: var(--gold-light); }
  .contact-bar {
    width: 330px; min-height: 36px; padding: 6px 18px;
    background: linear-gradient(90deg, var(--gold-deep), var(--gold-light) 45%, var(--gold) 80%, var(--gold-deep));
    clip-path: polygon(0 0, 96% 0, 100% 50%, 96% 100%, 0 100%);
    font-family: "Montserrat", sans-serif; font-weight: 500;
    font-size: 15px; line-height: 1.3; color: var(--ink);
    display: flex; flex-direction: column; justify-content: center;
  }
  .contact-bar.tall { min-height: 56px; }
</style>
</head>
<body>
  <main class="card">
    <svg class="card-trim" viewBox="0 0 1000 572" aria-hidden="true">
      <defs>
        <linearGradient id="gold-band" x1="0" x2="1" y1="0" y2="0">
          <stop offset="0" stop-color="#8a5d22"/>
          <stop offset=".45" stop-color="#f3d08a"/>
          <stop offset=".8" stop-color="#c99a4a"/>
          <stop offset="1" stop-color="#8a5d22"/>
        </linearGradient>
      </defs>
      <polygon class="band-top" points="0,0 440,0 440,16 0,16" fill="url(#gold-band)"/>
      <polygon points="400,28 412,28 432,60 420,60" fill="url(#gold-band)"/>
      <polygon points="420,28 432,28 452,60 440,60" fill="url(#gold-band)"/>
      <polygon class="band-bottom" points="0,556 440,556 440,572 0,572" fill="url(#gold-band)"/>
      <polygon points="400,512 412,512 432,544 420,544" fill="url(#gold-band)"/>
      <polygon points="420,512 432,512 452,544 440,544" fill="url(#gold-band)"/>
    </svg>

    <div class="brand">
      <span class="brand-dot"></span>
      <span class="brand-name">Fresh Tarrow Work Post</span>
    </div>

    <section class="person">
      <h1 class="person-name">Dorian Vale</h1>
      <p class="person-role">General Manager</p>
    </section>

    <ul class="contacts">
      <li class="contact">
        <span class="contact-icon"><svg viewBox="0 0 24 24"><path d="M6.6 10.8a15 15 0 0 0 6.6 6.6l2.2-2.2a1 1 0 0 1 1-.25 11.4 11.4 0 0 0 3.6.57 1 1 0 0 1 1 1V20a1 1 0 0 1-1 1A17 17 0 0 1 3 4a1 1 0 0 1 1-1h3.5a1 1 0 0 1 1 1c0 1.25.2 2.45.57 3.6a1 1 0 0 1-.25 1z"/></svg></span>
        <span class="contact-bar">014 582 3071</span>
      </li>
      <li class="contact">
        <span class="contact-icon"><svg viewBox="0 0 24 24"><path d="M7 2h10a2 2 0 0 1 2 2v16a2 2 0 0 1-2 2H7a2 2 0 0 1-2-2V4a2 2 0 0 1 2-2zm0 3v13h10V5zm5 14.2a1 1 0 1 0 0 .1z"/></svg></span>
        <span class="contact-bar">014 582 3071</span>
      </li>
      <li class="contact">
        <span class="contact-icon"><svg viewBox="0 0 24 24"><path d="M3 5h18v14H3zm2 2v.5l7 4.5 7-4.5V7zm0 2.9V17h14V9.9l-7 4.5z"/></svg></span>
        <span class="contact-bar">dvale@mailpost.example</span>
      </li>
      <li class="contact">
        <span class="contact-icon"><svg viewBox="0 0 24 24"><path d="M12 2a10 10 0 1 0 0 20 10 10 0 0 0 0-20zm6.9 9h-3a15 15 0 0 0-1.4-6A8 8 0 0 1 18.9 11zM12 4.1A13 13 0 0 1 13.9 11h-3.8A13 13 0 0 1 12 4.1zM9.5 5a15 15 0 0 0-1.4 6h-3A8 8 0 0 1 9.5 5zM5.1 13h3a15 15 0 0 0 1.4 6A8 8 0 0 1 5.1 13zm6.9 6.9A13 13 0 0 1 10.1 13h3.8a13 13 0 0 1-1.9 6.9zm2.5-.9a15 15 0 0 0 1.4-6h3a8 8 0 0 1-4.4 6z"/></svg></span>
        <span class="contact-bar">www.harbinworkpost.example</span>
      </li>
      <li class="contact">
        <span class="contact-icon"><svg viewBox="0 0 24 24"><path d="M12 2a7 7 0 0 0-7 7c0 5.2 7 13 7 13s7-7.8 7-13a7 7 0 0 0-7-7zm0 9.5A2.5 2.5 0 1 1 12 6.5a2.5 2.5 0 0 1 0 5z"/></svg></span>
        <span class="contact-bar tall"><span>42 Corrin Lane,</span><span>5th Floor North</span></span>
      </li>
    </ul>
  </main>
</body>
</html>
```